Website design for learning and development business

I need a logo for my new business based in Australasia. I am a kiwi who is a creative change maker working in the Learning & development space. I design experiential learning opportunities for businesses to grow and nurture their tribes. I take a holistic look at an organisation and analyse what is needed to build a positive culture with a growth mindset woven into their DNA. I would like to see designs that are based on the following word snaps - creative, interesting, tribal, journey, adaptability, engaging, fluid, architectural, bespoke, courageous, challenging .I have the logo (attached) and I Need a startup business website designed. I am a Learning and development professional who is looking at going out on my own and establishing my own business. I would like a website designed that people would go to to check out what I do, how I do, what skills I have and how to contact me. Also room for a blog/articles.

Target Market(s)

Small to medium business

Industry/Entity Type

Self employed training and consultancy company

Number of Pages Required

5+ page

Requirements
Must have
• home page, about page, contact us page, blog page, search for us page
Nice to have
• Testimonials,

```html
<!DOCTYPE html>
<html lang="en">
<head>
<meta charset="utf-8">
<title>Tarawa Learning — Home</title>
<link href="https://fonts.googleapis.com/css2?family=Lato:wght@400;700;900&family=Poppins:wght@400;500&display=swap" rel="stylesheet">
<style>
:root{
  --green:#3aaa35;
  --green-dark:#2e8f2a;
  --black:#000;
  --ink:#1d1d1d;
  --muted:#555;
  --mint:#f1f7ee;
  --field:#dedede;
  --white:#fff;
}
*{box-sizing:border-box;margin:0;padding:0}
html,body{width:1200px;height:3270px;overflow:hidden}
body{font-family:'Lato',sans-serif;color:var(--ink);background:var(--white)}
.page{width:1200px;height:3270px;position:relative}
.container{width:760px;margin:0 auto;position:relative}
.btn{display:inline-flex;align-items:center;gap:8px;background:var(--green);color:var(--white);font-size:12px;text-transform:uppercase;padding:0 16px;height:32px;text-decoration:none;letter-spacing:.3px}
.btn .ring{width:10px;height:10px;border:1.5px solid var(--white);border-radius:50%}
.section-title{text-align:center;font-size:30px;font-weight:400;letter-spacing:.5px;color:var(--ink)}
.section-mark{display:block;width:22px;height:22px;margin:0 auto 14px;border-radius:50%;background:var(--green)}

/* header + hero */
.hero{height:582px;position:relative;background:var(--black)}
.hero-photo{position:absolute;left:0;top:78px;width:1200px;height:504px;background:linear-gradient(90deg,#f4f1ee 0%,#e9e4df 35%,#9aa6b8 62%,#3d4c6b 85%,#2a3552 100%)}
.brand-tab{position:absolute;left:0;top:0;width:450px;height:102px;background:var(--black);clip-path:polygon(0 0,100% 0,100% 76%,96% 100%,0 100%)}
.brand{position:absolute;left:222px;top:40px;display:flex;align-items:center;gap:10px;color:var(--white);font-weight:900;font-size:24px;letter-spacing:1px;text-transform:uppercase}
.brand .dot{width:14px;height:14px;border-radius:50%;background:var(--green)}
.nav{position:absolute;right:220px;top:30px;display:flex;align-items:center}
.nav a{color:var(--white);font-size:11px;font-weight:700;text-decoration:none;padding:0 20px;border-left:1px solid #666;line-height:14px}
.nav a:first-child{border-left:none;color:var(--green)}
.hero-copy{position:absolute;left:222px;top:255px;width:410px}
.hero-copy h1{font-size:35px;font-weight:900;letter-spacing:-.3px;color:#111;margin-bottom:10px}
.hero-copy p{font-size:13px;line-height:20px;color:#222;margin-bottom:20px}
.dots{display:flex;gap:8px;margin-top:30px}
.dots span{width:10px;height:10px;border:1.5px solid #222;border-radius:50%}
.dots span.on{background:#222}

/* about */
.about{height:417px;padding-top:62px}
.about .container{display:flex;gap:40px}
.about-photo{width:418px;height:293px;background:linear-gradient(135deg,#cfc8bf,#8b8580 55%,#5d6066)}
.about-copy{width:300px;padding-top:14px}
.about-copy h2{font-size:22px;font-weight:400;color:var(--green);padding-bottom:6px;border-bottom:1px solid var(--green);margin-bottom:14px}
.about-copy p{font-size:9.5px;line-height:16px;color:var(--muted);text-align:justify;margin-bottom:10px}

/* intro band */
.band{height:305px;background:linear-gradient(90deg,#d7dfd3,#eef2ea 30%,#eef2ea 70%,#d4dccf);text-align:center;padding-top:58px}
.band h3{font-size:18px;font-weight:400;color:var(--green);margin-bottom:10px}
.band p{width:760px;margin:0 auto 24px;font-size:13.5px;line-height:24px;color:#333}

/* testimonials */
.testimonials{height:427px;padding-top:58px;text-align:center;position:relative}
.avatar{width:96px;height:96px;border-radius:50%;margin:22px auto 14px;background:radial-gradient(circle,#c9b8a6,#7a6d62)}
.client-name{font-size:13px;font-weight:700;letter-spacing:.3px}
.client-role{font-size:9px;color:var(--green);margin:2px 0 8px}
.quote-mark{position:absolute;left:312px;top:300px;font-size:120px;line-height:1;color:#e2e2e2;font-family:'Lato',sans-serif;font-weight:900}
.testimonials blockquote{position:relative;width:540px;margin:0 auto;font-family:'Poppins',sans-serif;font-size:9.5px;line-height:17px;color:#555}
.tdots{display:flex;gap:9px;justify-content:center;margin-top:18px}
.tdots span{width:10px;height:10px;border-radius:50%;background:#aaa}
.tdots span.on{background:var(--green)}

/* blog */
.blog{height:520px;background:var(--mint);padding-top:58px}
.cards{display:flex;gap:18px;justify-content:center;margin-top:30px}
.card{width:240px;height:310px;background:var(--white);border:1px solid #e4e4e4;position:relative}
.card-photo{height:164px;background:linear-gradient(135deg,#59697f,#2f3d52 60%,#8a7a6a)}
.date{position:absolute;left:12px;top:150px;width:36px;height:36px;border-radius:50%;background:var(--green);color:var(--white);font-size:8px;font-weight:700;display:flex;flex-direction:column;align-items:center;justify-content:center;line-height:10px;border:2px solid var(--white)}
.card-body{padding:30px 12px 0}
.card-body h4{font-size:11px;font-weight:700;line-height:17px;margin-bottom:10px}
.card-body p{font-family:'Poppins',sans-serif;font-size:9px;line-height:15px;color:#666;margin-bottom:10px}
.read-more{font-size:9px;font-weight:700;color:#222;text-decoration:none}
.read-more b{color:var(--green)}

/* contact */
.contact{height:437px;position:relative}
.contact-photo{position:absolute;left:0;top:0;width:660px;height:437px;background:linear-gradient(90deg,#8fa5b8 0%,#b8c8d4 40%,#e2eaee 70%,rgba(255,255,255,0) 100%)}
.contact-form{position:absolute;left:598px;top:70px;width:380px}
.contact-form h2{font-size:30px;font-weight:400;text-align:center;margin-bottom:16px;margin-top:0}
.contact-form .section-mark{margin-bottom:10px}
.fields{display:grid;grid-template-columns:1fr 1fr;gap:4px}
.field{background:var(--field);height:36px;font-size:9px;color:#666;padding:12px 10px;text-transform:uppercase}
.field.message{grid-column:1/3;height:100px}
.contact-form .btn{margin-top:24px}

/* clients */
.clients{height:277px;background:var(--mint);padding-top:58px}
.logos{display:flex;gap:10px;justify-content:center;margin-top:20px}
.logo-box{width:143px;height:60px;border:2px solid #d4d4d4;background:var(--white);display:flex;align-items:center;justify-content:center;font-size:13px;font-weight:700;color:#9a9a9a}
.logo-box.active{border-color:var(--green);color:#222}

/* footer */
.footer{height:305px;background:var(--black);color:var(--white);position:relative}
.footer .container{display:flex;padding-top:50px}
.footer-brand{width:400px;padding-top:38px}
.footer-brand .brand-name{display:flex;align-items:center;gap:10px;font-weight:900;font-size:26px;letter-spacing:1px;text-transform:uppercase;margin-bottom:12px}
.footer-brand .brand-name .dot{width:14px;height:14px;border-radius:50%;background:var(--green)}
.footer-brand p{font-size:9px;line-height:15px;width:310px;color:#ddd}
.social{display:flex;gap:8px;margin-top:14px}
.social span{width:12px;height:12px;border-radius:50%;background:var(--white)}
.footer-col{width:198px}
.footer-col h5{font-size:12px;font-weight:700;margin-bottom:10px}
.footer-col hr{width:30px;border:0;border-top:2px solid var(--white);margin-bottom:16px}
.footer-col a{display:block;color:var(--white);font-size:9px;text-decoration:none;margin-bottom:13px}
.contact-line{display:flex;gap:8px;font-size:9px;margin-bottom:16px;align-items:flex-start;line-height:13px}
.copyright{position:absolute;left:220px;right:220px;bottom:20px;border-top:1px solid #333;padding-top:14px;text-align:center;font-size:9px;color:#ddd}
</style>
</head>
<body>
<div class="page">

  <header class="hero">
    <div class="hero-photo" role="img" aria-label="Photo of two smiling businessmen in suits reviewing a tablet at a desk"></div>
    <div class="brand-tab"></div>
    <div class="brand"><span class="dot"></span>Tarawa Learning</div>
    <nav class="nav">
      <a href="#">HOME</a><a href="#">ABOUT US</a><a href="#">TESTIMONIALS</a><a href="#">BLOG</a><a href="#">CONTACT US</a>
    </nav>
    <div class="hero-copy">
      <h1>TARAWA LEARNING</h1>
      <p>I am a kiwi who is a creative change maker working in the Learning &amp; development space. I design experiential learning opportunities for businesses to grow and nurture their tribes.</p>
      <a class="btn" href="#">Learn More <span class="ring"></span></a>
      <div class="dots"><span></span><span></span><span class="on"></span><span></span></div>
    </div>
  </header>

  <section class="about">
    <div class="container">
      <div class="about-photo" role="img" aria-label="Photo of a team gathered around a laptop in a bright office"></div>
      <div class="about-copy">
        <h2>TARAWA LEARNING</h2>
        <p>I am a kiwi who is a creative change maker working in the Learning &amp; development space. I design experiential learning opportunities for businesses to grow and nurture their tribes. I take a holistic look at an organisation and analyse what is needed to build a positive culture with a growth mindset woven into their DNA.</p>
        <p>It is a long established fact that a reader will be distracted by the readable content of a page when looking at its layout. The point of using Lorem Ipsum is that it has a more-or-less normal distribution of letters, as opposed</p>
        <a class="btn" href="#">Read More <span class="ring"></span></a>
      </div>
    </div>
  </section>

  <section class="band" role="region" aria-label="Introduction over a faded city office backdrop">
    <h3>Lorem Ipsum is simply dummy text of the printing and typesetting industry.</h3>
    <p>There are many variations of passages of Lorem Ipsum available, but the majority have suffered alteration in some form, by injected humour, or randomised words which don't look even slightly believable. If you are going to use a passage of Lorem Ipsum, you need to be sure there isn't anything embarrassing hidden in the middle of text. All the Lorem Ipsum generators on the Internet tend to repeat</p>
    <a class="btn" href="#">Contact Us <span class="ring"></span></a>
  </section>

  <section class="testimonials">
    <span class="section-mark"></span>
    <h2 class="section-title">TESTIMONIALS</h2>
    <div class="avatar" role="img" aria-label="Client portrait photo"></div>
    <div class="client-name">CLIENT'S NAME</div>
    <div class="client-role">DESIGNATION</div>
    <div class="quote-mark">&ldquo;</div>
    <blockquote>Lorem ipsum dolor sit amet, consectetur adipiscing elit, sed do eiusmod tempor incididunt ut labore et dolore magna aliqua. Ut enim ad minim veniam, quis nostrud exercitation ullamco laboris nisi ut aliquip ex ea commodo consequat. Duis aute irure dolor in reprehenderit in voluptate.</blockquote>
    <div class="tdots"><span></span><span></span><span class="on"></span><span></span></div>
  </section>

  <section class="blog">
    <span class="section-mark"></span>
    <h2 class="section-title">LATEST BLOG</h2>
    <div class="cards">
      <article class="card">
        <div class="card-photo" role="img" aria-label="Photo of colleagues working together at laptops"></div>
        <div class="date"><span>29</span><span>JUL</span></div>
        <div class="card-body">
          <h4>Lorem ipsum dolor sit amet, consectetur adipiscing elit, sed do eiusmod</h4>
          <p>There are many variations of passages of Lorem Ipsum available, but the majority...</p>
          <a class="read-more" href="#">READ MORE <b>&#9656;</b></a>
        </div>
      </article>
      <article class="card">
        <div class="card-photo" role="img" aria-label="Photo of a team meeting around a wooden table"></div>
        <div class="date"><span>29</span><span>JUL</span></div>
        <div class="card-body">
          <h4>Lorem ipsum dolor sit amet, consectetur adipiscing elit, sed do eiusmod</h4>
          <p>There are many variations of passages of Lorem Ipsum available, but the majority...</p>
          <a class="read-more" href="#">READ MORE <b>&#9656;</b></a>
        </div>
      </article>
      <article class="card">
        <div class="card-photo" role="img" aria-label="Photo of business people talking in a busy office"></div>
        <div class="date"><span>29</span><span>JUL</span></div>
        <div class="card-body">
          <h4>Lorem ipsum dolor sit amet, consectetur adipiscing elit, sed do eiusmod</h4>
          <p>There are many variations of passages of Lorem Ipsum available, but the majority...</p>
          <a class="read-more" href="#">READ MORE <b>&#9656;</b></a>
        </div>
      </article>
    </div>
  </section>

  <section class="contact">
    <div class="contact-photo" role="img" aria-label="Photo of a man working on a laptop on a sofa by a city window"></div>
    <form class="contact-form">
      <span class="section-mark"></span>
      <h2>GET IN TOUCH WITH US</h2>
      <div class="fields">
        <div class="field">Name</div><div class="field">Phone</div>
        <div class="field">Email</div><div class="field">Subject</div>
        <div class="field message">Message</div>
      </div>
      <a class="btn" href="#">Send Now <span class="ring"></span></a>
    </form>
  </section>

  <section class="clients">
    <span class="section-mark"></span>
    <h2 class="section-title">OUR CLIENTS</h2>
    <div class="logos">
      <div class="logo-box">Northbay</div>
      <div class="logo-box active">Harbourline</div>
      <div class="logo-box">Kowhai Co</div>
      <div class="logo-box">Ridgeway</div>
      <div class="logo-box">Fernhill</div>
    </div>
  </section>

  <footer class="footer">
    <div class="container">
      <div class="footer-brand">
        <div class="brand-name"><span class="dot"></span>Tarawa Learning</div>
        <p>Lorem ipsum dolor sit amet, consectetur adipiscing elit, sed do eiusmod tempor incididunt ut labore et dolore magna aliqua. Ut enim ad minim veniam, quis nostrud exercitation ullamco laboris nisi ut.</p>
        <div class="social" aria-label="Social links"><span></span><span></span><span></span></div>
      </div>
      <div class="footer-col">
        <h5>QUICK LINKS</h5><hr>
        <a href="#">HOME</a><a href="#">ABOUT US</a><a href="#">TESTIMONIALS</a><a href="#">BLOG</a><a href="#">CONTACT US</a>
      </div>
      <div class="footer-col">
        <h5>CONTACT US</h5><hr>
        <div class="contact-line">
          <svg width="11" height="11" viewBox="0 0 24 24"><path fill="#3aaa35" d="M6.6 10.8a15 15 0 0 0 6.6 6.6l2.2-2.2a1 1 0 0 1 1-.25 11.4 11.4 0 0 0 3.6.57 1 1 0 0 1 1 1V20a1 1 0 0 1-1 1A17 17 0 0 1 3 4a1 1 0 0 1 1-1h3.5a1 1 0 0 1 1 1c0 1.25.2 2.45.57 3.6a1 1 0 0 1-.25 1z"/></svg>
          <span>021 555 0142</span>
        </div>
        <div class="contact-line">
          <svg width="11" height="11" viewBox="0 0 24 24"><rect x="2" y="5" width="20" height="14" fill="none" stroke="#3aaa35" stroke-width="2"/><path d="M2 5l10 8 10-8" fill="none" stroke="#3aaa35" stroke-width="2"/></svg>
          <span>hello@tarawalearning.co</span>
        </div>
        <div class="contact-line">
          <svg width="11" height="13" viewBox="0 0 24 28"><path d="M12 2a8 8 0 0 0-8 8c0 6 8 16 8 16s8-10 8-16a8 8 0 0 0-8-8z" fill="none" stroke="#3aaa35" stroke-width="2"/><circle cx="12" cy="10" r="3" fill="#3aaa35"/></svg>
          <span>234 Lorem ipsum dolor<br>street, consectetur adipiscing</span>
        </div>
      </div>
    </div>
    <div class="copyright">Copyright 2021 TARAWA LEARNING. All Rights Are Reserved.</div>
  </footer>

</div>
</body>
</html>
```